Invitation Design Project

I need a customized graphic design for my wedding invitation.I want it to be non-traditional wedding invite. The design in mind is like a movie poster graphics while adopting 'the brighter days of the islands' font style and colors that create a light mood at the front page.Inside pages can be similar to movie posters with dark background similar to that of Ashen warden.Wedding related art/graphics can be integrated within the design.Wordings can be discussed later.

Industry/Entity Type

Graphic Design

Requirements
Must have
• Other must have features are our pictures as couple which will be sent .
Nice to have
• we would like to have the words

"our wedding.

more fun if you'll come!"

on the front cover.

```html
<!DOCTYPE html>
<html lang="en">
<head>
<meta charset="utf-8">
<title>Wedding Invitation</title>
<link rel="stylesheet" href="https://fonts.googleapis.com/css2?family=Nunito:wght@800;900&family=Archivo+Narrow:wght@500;600&display=swap">
<style>
  :root {
    --paper: #ffffff;
    --night: #050708;
    --sky: #5fc8d4;
    --sky-deep: #1f7f8a;
    --navy: #2d2a79;
    --navy-band: #25309a;
    --blue: #3f6bb4;
    --light-blue: #47a6dc;
    --orange: #f4a01c;
    --gold: #f2a626;
    --red: #e1272d;
    --dark-red: #a61c22;
    --maroon: #9a1a1c;
    --stripe-orange: #f08a2c;
    --stripe-yellow: #f7d21c;
    --fold: #777777;
  }
  * { box-sizing: border-box; margin: 0; padding: 0; }
  html, body { width: 1200px; height: 900px; overflow: hidden; background: var(--paper); }
  .canvas { position: relative; width: 1200px; height: 900px; background: var(--paper); }

  .inside-panel {
    position: absolute; left: 0; top: 17px; width: 594px; height: 842px;
    background: var(--night); overflow: hidden;
  }
  .city-photo {
    position: absolute; inset: 0;
    background:
      radial-gradient(ellipse 45% 40% at 58% 38%, var(--sky) 0%, var(--sky-deep) 45%, transparent 80%),
      linear-gradient(160deg, #0a1214 0%, #050708 60%, #0b1416 100%);
  }
  .invite-text {
    position: absolute; left: 0; width: 100%; text-align: center;
    font-family: "Archivo Narrow", "Arial Narrow", sans-serif;
  }
  .invite-intro { top: 618px; font-size: 16px; font-weight: 500; color: var(--maroon); letter-spacing: -0.2px; }
  .couple-names { top: 670px; font-size: 29px; font-weight: 600; color: var(--gold); letter-spacing: 1px; }
  .couple-names .joiner { color: var(--red); margin: 0 14px; }
  .event-date { top: 768px; font-size: 17px; font-weight: 600; color: var(--red); line-height: 27px; }
  .event-date .venue { color: var(--light-blue); }

  .fold-line { position: absolute; left: 595px; top: 0; height: 900px; border-left: 1.5px dashed var(--fold); }

  .cover-panel {
    position: absolute; left: 597px; top: 17px; width: 603px; height: 842px; overflow: hidden;
    background: linear-gradient(180deg, var(--navy-band) 0%, var(--stripe-orange) 6%, var(--stripe-yellow) 12%, var(--stripe-orange) 18%, var(--red) 100%);
  }
  .stripe-art {
    position: absolute; inset: 0;
    background:
      linear-gradient(90deg, var(--light-blue) 0 8%, var(--stripe-orange) 8% 20%, var(--stripe-yellow) 20% 26%, var(--red) 26% 34%, var(--navy-band) 34% 42%, var(--stripe-orange) 42% 70%, var(--light-blue) 70% 80%, var(--red) 80% 100%);
    opacity: 0.85;
  }
  .headline-band { position: absolute; left: 0; width: 100%; }
  .band-peach { top: 150px; height: 92px; background: rgba(250, 200, 180, 0.85); }
  .band-sky { top: 242px; height: 90px; background: rgba(170, 195, 235, 0.9); }
  .band-lavender { top: 332px; height: 118px; background: rgba(150, 150, 215, 0.9); }
  .band-navy { top: 450px; height: 30px; background: var(--navy-band); }

  .headline {
    position: absolute; left: 42px; top: 168px;
    font-family: "Nunito", "Varela Round", sans-serif; font-weight: 900;
    font-size: 66px; line-height: 94px; color: var(--navy); letter-spacing: -1.5px;
  }
  .headline .line { display: block; white-space: nowrap; }
  .c-navy { color: var(--navy); } .c-blue { color: var(--blue); } .c-light { color: var(--light-blue); }
  .c-orange { color: var(--orange); } .c-red { color: var(--red); } .c-dark-red { color: var(--dark-red); }

  .couple-photo {
    position: absolute; left: 306px; top: 467px; width: 243px; height: 340px;
    background: radial-gradient(ellipse at 50% 45%, #8a9a8e 0%, #5d6b62 55%, #3c4640 100%);
    box-shadow: 0 0 12px 6px rgba(60, 70, 64, 0.6);
  }
</style>
</head>
<body>
<main class="canvas">
  <section class="inside-panel">
    <div class="city-photo" role="img" aria-label="Photograph looking up at dark skyscrapers against a cyan cloudy sky"></div>
    <p class="invite-text invite-intro">Together with our families join us in celebrating the marriage of</p>
    <p class="invite-text couple-names">XXXX XXXXX <span class="joiner">and</span> YYYYY YYYY</p>
    <p class="invite-text event-date">FRIDAY &nbsp;21 OCTOBER &nbsp;two thousand and twelve<br>seven o’clock in the evening at <span class="venue">$%@&amp;’@828u87`%$#</span></p>
  </section>

  <div class="fold-line" aria-hidden="true"></div>

  <section class="cover-panel">
    <div class="stripe-art" role="img" aria-label="Woven pattern of orange, yellow, red and blue stripes"></div>
    <div class="headline-band band-peach"></div>
    <div class="headline-band band-sky"></div>
    <div class="headline-band band-lavender"></div>
    <div class="headline-band band-navy"></div>
    <h1 class="headline">
      <span class="line">our <span class="c-navy">W</span><span class="c-blue">e</span><span class="c-light">d</span><span class="c-light">d</span><span class="c-orange">i</span><span class="c-red">n</span><span class="c-dark-red">g</span> <span class="c-dark-red">.</span></span>
      <span class="line">more <span class="c-orange">fun</span></span>
      <span class="line">if you’ll <span class="c-red">come!</span></span>
    </h1>
    <div class="couple-photo" role="img" aria-label="Photograph of the couple standing together in front of a waterfall"></div>
  </section>
</main>
</body>
</html>
```